Zumbly - New Payment App for Student

Zum-bly - A Payment App for student to make payment, track own expenses and practice good dietary habits. The App theme is Fun and excitement.
Target User: Secondary Student aged 13-18
Look and Feel: Fun, excitement and simple.
Screen 1
Login to the app using thumbprints or password
Screen 2
Display the balance
Wallet balance >>> go to screen 3 to display transaction history
Gamification balance - points + badges >>> go to screen 3
Button to make payment
Screen 2-1
Allow them to do payment
Click “Pay”
Display QR code
scanning by merchant
Payment made
Notification received
The transaction history will be shown up
Screen 2-2
Allow them to top up (alternatively to parent Top-up using credit card)
Click “Top Up”
Display QR code
Pass the cash to merchant
scanning by merchant
Payment made
Notification received
The new balance will be shown up
Screen 3
Display more details on transaction history
Payment history + gamification history (gain/redeem points)
E.g. 14 Nov Canteen purchase $5.40
- Banana +30 points
- Milk +10 points
Screen 4 (play a game to earn point)
Introduce some trivial games (while waiting in line at cafeteria or school store) to gain some points
Crosswords
Puzzle
Screen 5 (Display achievements)
Leaderboard
Where the individual stands in the class
Where the class stands overall in school
Badges
Level
Achievements
For more, please go to our website http://www.zumbly-pay.example/
Target Market(s)
Secondary School Student aged 13-18
Industry/Entity Type
Education
Logo Text
zumbly
Look and feel

```html
<!DOCTYPE html>
<html lang="en">
<head>
<meta charset="utf-8">
<title>Zumbly – Transaction History</title>
<link rel="stylesheet" href="https://fonts.googleapis.com/css2?family=Lato:wght@400;700&display=swap">
<style>
  :root {
    --screen-bg: #d4e7e7;
    --ink: #3b3d40;
    --ink-soft: #45474a;
    --coin: #fdd31d;
    --coin-edge: #c9a616;
    --icon-line: #5a4a0c;
    --divider: #f4fafa;
  }
  * { margin: 0; padding: 0; box-sizing: border-box; }
  html, body { width: 675px; height: 1200px; overflow: hidden; }
  body {
    background: var(--screen-bg);
    font-family: "Lato", sans-serif;
    color: var(--ink);
    position: relative;
  }
  .status-bar {
    position: absolute; top: 0; left: 0; width: 675px; height: 36px;
    font-size: 17px; color: var(--ink);
  }
  .status-bar .signal { position: absolute; left: 12px; top: 11px; }
  .status-bar .time { position: absolute; left: 0; width: 675px; top: 8px; text-align: center; }
  .status-bar .battery { position: absolute; right: 10px; top: 8px; display: flex; align-items: center; gap: 6px; }
  .nav-bar { position: absolute; top: 52px; left: 0; width: 675px; height: 56px; }
  .nav-bar .back {
    position: absolute; left: 15px; top: 8px; display: flex; align-items: center; gap: 12px;
    font-size: 30px; color: var(--ink-soft);
  }
  .nav-bar .title {
    position: absolute; left: 0; width: 670px; top: 9px; text-align: center;
    font-size: 31px; font-weight: 700; color: var(--ink);
  }
  .nav-bar .refresh { position: absolute; right: 32px; top: 6px; }
  .transactions { list-style: none; }
  .transaction {
    position: absolute; left: 53px; width: 570px; height: 80px;
    display: flex; align-items: center;
  }
  .coin {
    width: 72px; height: 76px; position: relative; flex: none; margin-left: -1px;
  }
  .coin::before {
    content: ""; position: absolute; left: 0; top: 5px; width: 72px; height: 72px;
    border-radius: 50%; background: var(--coin-edge);
  }
  .coin::after {
    content: ""; position: absolute; left: 0; top: 0; width: 72px; height: 72px;
    border-radius: 50%; background: var(--coin);
  }
  .coin svg { position: absolute; left: 18px; top: 16px; width: 36px; height: 40px; z-index: 1; }
  .item-name { margin-left: 16px; font-size: 26px; font-weight: 700; flex: 1; }
  .amount { font-size: 21px; font-weight: 400; color: var(--ink-soft); }
  .divider {
    position: absolute; left: 53px; width: 570px; height: 2px; background: var(--divider);
  }
</style>
</head>
<body>
  <header class="status-bar">
    <svg class="signal" width="90" height="14" viewBox="0 0 90 14" aria-hidden="true">
      <g fill="#3b3d40">
        <circle cx="5" cy="7" r="4.5"/><circle cx="16" cy="7" r="4.5"/><circle cx="27" cy="7" r="4.5"/>
        <circle cx="38" cy="7" r="4.5"/><circle cx="49" cy="7" r="4.5"/>
      </g>
      <g fill="none" stroke="#3b3d40" stroke-width="2.2" stroke-linecap="round">
        <path d="M62 5 Q72 -3 82 5"/><path d="M65.5 8.5 Q72 3 78.5 8.5"/>
      </g>
      <circle cx="72" cy="12" r="1.8" fill="#3b3d40"/>
    </svg>
    <div class="time">9:41 AM</div>
    <div class="battery">
      <span>100%</span>
      <svg width="44" height="16" viewBox="0 0 44 16" aria-hidden="true">
        <rect x="1" y="1" width="38" height="14" rx="2" fill="none" stroke="#3b3d40" stroke-width="1.5"/>
        <rect x="3" y="3" width="34" height="10" fill="#3b3d40"/>
        <rect x="40.5" y="5" width="2.5" height="6" fill="#3b3d40"/>
      </svg>
    </div>
  </header>

  <nav class="nav-bar">
    <div class="back">
      <svg width="22" height="36" viewBox="0 0 22 36" aria-hidden="true">
        <path d="M18 3 L4 18 L18 33" fill="none" stroke="#45474a" stroke-width="4" stroke-linecap="round" stroke-linejoin="round"/>
      </svg>
      <span>Back</span>
    </div>
    <h1 class="title">Transaction History</h1>
    <svg class="refresh" width="44" height="44" viewBox="0 0 44 44" aria-label="Refresh" role="img">
      <path d="M14 8 A17 17 0 1 0 30 8" fill="none" stroke="#3b3d40" stroke-width="5.5"/>
      <path d="M6 4 L19 3 L16 15 Z" fill="#3b3d40"/>
    </svg>
  </nav>

  <ul class="transactions">
    <li class="transaction" style="top:139px">
      <span class="coin"><svg viewBox="0 0 36 40" fill="none" stroke="#5a4a0c" stroke-width="1.6" stroke-linejoin="round">
        <path d="M10 12 L14 4 H26 L26 12 Z M10 12 V36 H22 V12 M22 12 L26 4 M22 36 L28 32 V12 L26 4"/><rect x="12" y="1" width="12" height="3"/></svg></span>
      <span class="item-name">Milk</span><span class="amount">$580.88</span>
    </li>
    <li class="divider" style="top:250px"></li>

    <li class="transaction" style="top:282px">
      <span class="coin"><svg viewBox="0 0 36 40" fill="none" stroke="#5a4a0c" stroke-width="1.6" stroke-linejoin="round">
        <path d="M9 8 H27 L25 36 H11 Z"/><rect x="8" y="4" width="20" height="4" rx="1"/><rect x="11" y="1" width="14" height="3"/><circle cx="18" cy="21" r="4"/><path d="M10 16 H26 M10 26 H26"/></svg></span>
      <span class="item-name">Coffee</span><span class="amount">$580.88</span>
    </li>
    <li class="divider" style="top:391px"></li>

    <li class="transaction" style="top:424px">
      <span class="coin"><svg viewBox="0 0 36 40" fill="none" stroke="#5a4a0c" stroke-width="1.6" stroke-linejoin="round">
        <path d="M2 16 Q8 8 12 14 T22 10 T32 4 L36 10 Q30 14 26 18 T16 24 T6 30 Z"/><path d="M5 22 Q10 16 14 20 T24 16 T33 9"/></svg></span>
      <span class="item-name">Bacon</span><span class="amount">$580.88</span>
    </li>
    <li class="divider" style="top:533px"></li>

    <li class="transaction" style="top:567px">
      <span class="coin"><svg viewBox="0 0 36 40" fill="none" stroke="#5a4a0c" stroke-width="1.6">
        <ellipse cx="25" cy="18" rx="8" ry="10"/><ellipse cx="14" cy="26" rx="12" ry="8" fill="#fdd31d"/></svg></span>
      <span class="item-name">Eggs</span><span class="amount">$580.88</span>
    </li>
    <li class="divider" style="top:673px"></li>

    <li class="transaction" style="top:710px">
      <span class="coin"><svg viewBox="0 0 36 40" fill="none" stroke="#5a4a0c" stroke-width="1.6" stroke-linejoin="round">
        <path d="M3 18 Q3 6 18 6 Q33 6 33 18 Z"/><path d="M2 22 Q6 19 10 22 T18 22 T26 22 T34 22"/><rect x="2" y="25" width="32" height="4" rx="2"/><path d="M4 31 H32 Q32 35 28 35 H8 Q4 35 4 31 Z"/>
        <g fill="#5a4a0c" stroke="none"><circle cx="12" cy="12" r="1"/><circle cx="18" cy="10" r="1"/><circle cx="24" cy="12" r="1"/><circle cx="15" cy="15" r="1"/><circle cx="21" cy="15" r="1"/></g></svg></span>
      <span class="item-name">Hamburger</span><span class="amount">$580.88</span>
    </li>
    <li class="divider" style="top:822px"></li>

    <li class="transaction" style="top:852px">
      <span class="coin"><svg viewBox="0 0 36 40" fill="none" stroke="#5a4a0c" stroke-width="1.6" stroke-linejoin="round">
        <path d="M14 14 Q22 6 32 12 Q28 22 20 22 Z"/><path d="M14 14 Q6 18 8 30 L12 36 Q12 28 16 24 L20 22"/><path d="M8 30 Q2 26 4 20 L10 16"/><path d="M18 16 L24 20 M22 12 L27 18"/></svg></span>
      <span class="item-name">Baked Bread</span><span class="amount">$580.88</span>
    </li>
  </ul>
</body>
</html>
```